Tandrel needs stationery design

We need desings for presentation cards and letter head for our company. It would be better that the letterhead uses our logo with white background and the presentation card the logo with the black background for the back of the card and the text (name, phone

Colors
0455a3
ec1f27
000000

Requirements
Must have
• Use company logo and colors

```html
<!DOCTYPE html>
<html lang="en">
<head>
<meta charset="utf-8">
<title>Tandrel Stationery</title>
<link href="https://fonts.googleapis.com/css2?family=Hind:wght@400;500;600&display=swap" rel="stylesheet">
<style>
  :root {
    --brand-blue: #0455a3;
    --brand-red: #ec1f27;
    --ink: #000000;
    --text: #3a3a3a;
    --muted: #666666;
    --paper: #ffffff;
    --paper-shade: #ececec;
    --backdrop: #6b6b6b;
    --card-black: #1b1b1b;
    --logo-grey: #8a8a8a;
  }
  * { margin: 0; padding: 0; box-sizing: border-box; }
  html, body { width: 760px; height: 1200px; overflow: hidden; }
  body {
    background: var(--backdrop);
    font-family: "Hind", Arial, sans-serif;
    color: var(--text);
    position: relative;
  }

  /* Letterhead */
  .letterhead {
    position: absolute;
    left: 150px; top: 30px;
    width: 460px; height: 650px;
    background: linear-gradient(180deg, var(--paper) 0%, var(--paper-shade) 100%);
    box-shadow: 0 6px 18px rgba(0,0,0,.35);
    padding: 52px 30px 0 30px;
  }
  .wordmark {
    font-weight: 600;
    letter-spacing: 2px;
    color: var(--ink);
    display: flex; align-items: center; gap: 7px;
  }
  .wordmark .mark-square { width: 9px; height: 9px; background: var(--brand-red); }
  .letterhead .wordmark { font-size: 26px; }

  .recipient { margin-top: 100px; font-size: 9.5px; line-height: 15px; color: #333; }
  .recipient .salutation { color: var(--brand-blue); font-weight: 500; }

  .letter-body { margin-top: 22px; font-size: 9.2px; line-height: 14.8px; text-align: justify; color: #333; }
  .letter-body p + p { margin-top: 15px; }

  .closing { margin-top: 20px; font-size: 8px; color: #333; }
  .signature {
    display: block; width: 62px; height: 20px; margin: 4px 0 6px;
    background: linear-gradient(90deg, #d6d6d6, #c4c4c4);
    border-radius: 10px;
  }
  .closing .signer { font-size: 8.5px; }

  .letter-footer {
    position: absolute; left: 0; right: 0; bottom: 26px;
    text-align: center; font-size: 8.3px; line-height: 13px; color: #444;
  }
  .letter-footer .brand { color: var(--brand-blue); font-weight: 600; }

  .contact-line { display: inline-flex; align-items: center; gap: 4px; }
  .icon { width: 8px; height: 8px; flex: none; }
  .icon path, .icon rect, .icon circle { fill: var(--brand-red); }

  /* Business cards */
  .card {
    position: absolute; left: 200px;
    width: 360px; height: 205px;
    box-shadow: 0 5px 14px rgba(0,0,0,.4);
  }
  .card-back {
    top: 720px;
    background: var(--card-black);
    display: flex; align-items: center; justify-content: center;
  }
  .card-back .wordmark { font-size: 34px; color: var(--logo-grey); }

  .card-front { top: 960px; background: var(--paper); }
  .card-front .wordmark { position: absolute; left: 26px; top: 88px; font-size: 26px; }
  .card-divider {
    position: absolute; left: 196px; top: 54px;
    width: 1px; height: 88px; background: #555;
  }
  .card-contact { position: absolute; left: 212px; top: 58px; font-size: 9px; line-height: 13px; color: #444; }
  .card-contact .name { font-size: 14px; font-weight: 600; color: var(--brand-blue); letter-spacing: .5px; line-height: 16px; }
  .card-contact .role { font-size: 8.5px; color: var(--muted); margin-bottom: 8px; }
  .card-contact .web-strong { color: var(--brand-blue); font-weight: 600; }
  .card-address {
    position: absolute; left: 26px; bottom: 18px;
    font-size: 8.5px; color: #444;
  }
  .card-address .brand { color: var(--brand-blue); font-weight: 600; }
</style>
</head>
<body>

<svg width="0" height="0" style="position:absolute">
  <defs>
    <symbol id="icon-phone" viewBox="0 0 10 10"><path d="M2 0.5 L3.6 0.5 L4.2 3 L3 3.8 C3.6 5.2 4.8 6.4 6.2 7 L7 5.8 L9.5 6.4 L9.5 8 C9.5 9 8.8 9.5 8 9.5 C4 9.2 0.8 6 0.5 2 C0.5 1.2 1 0.5 2 0.5 Z"/></symbol>
    <symbol id="icon-mail" viewBox="0 0 10 10"><path d="M0.5 2 H9.5 V8 H0.5 Z M1.5 3 V7 H8.5 V3 L5 5.6 Z M2 3 L5 5 L8 3 Z" fill-rule="evenodd"/></symbol>
    <symbol id="icon-web" viewBox="0 0 10 10"><circle cx="5" cy="5" r="4.5"/></symbol>
  </defs>
</svg>

<section class="letterhead">
  <div class="wordmark"><span class="mark-square"></span>TANDREL</div>

  <div class="recipient">
    <div class="salutation">Dear Mr. Daniel Ward</div>
    <div>Resident Manager</div>
    <div>58 Orchard Lane</div>
    <div>Millbrook, OR</div>
  </div>

  <div class="letter-body">
    <p>Lorem ipsum dolor sit amet, consectetuer adipiscing elit, sed diam nonummy nibh euismod tincidunt ut laoreet dolore magna aliquam erat volutpat. Ut wisi enim ad minim veniam, quis nostrud exerci tation ullamcorper suscipit lobortis nisl ut aliquip ex ea commodo consequat. Lorem ipsum dolor sit amet, consectetuer adipiscing elit, sed diam nonummy nibh euismod tincidunt ut laoreet dolore magna aliquam erat volutpat. Ut wisi enim ad minim veniam, quis nostrud exerci tation ullamcorper suscipit lobortis nisl ut aliquip ex ea commodo consequat. Lorem ipsum dolor sit amet, consectetuer adipiscing elit, sed diam nonummy nibh euismod tincidunt ut laoreet dolore magna aliquam erat volutpat. Ut wisi enim ad minim veniam,</p>
    <p>consequat. Duis autem vel eum iriure dolor in hendrerit in vulputate velit esse molestie consequat, vel illum dolore eu feugiat nulla facilisis at vero eros et accumsan.</p>
  </div>

  <div class="closing">
    <div>sincerely</div>
    <span class="signature" role="img" aria-label="Handwritten signature of Daniel Ward"></span>
    <div class="signer">Daniel Ward</div>
  </div>

  <footer class="letter-footer">
    <div><span class="brand">Tandrel</span> – 412 W 9th St. Ste 210 Brayford, OH 45102</div>
    <div>
      <span class="contact-line"><svg class="icon"><use href="#icon-phone"/></svg>+555 014 2276</span> |
      <span class="contact-line"><svg class="icon"><use href="#icon-mail"/></svg>info@tandrel.com</span> |
      <span class="contact-line"><svg class="icon"><use href="#icon-web"/></svg>www.tandrel.com</span>
    </div>
  </footer>
</section>

<section class="card card-back">
  <div class="wordmark">TANDREL</div>
</section>

<section class="card card-front">
  <div class="wordmark"><span class="mark-square"></span>TANDREL</div>
  <div class="card-divider"></div>
  <div class="card-contact">
    <div class="name">OWEN HARLOW</div>
    <div class="role">Resident Manager</div>
    <div class="contact-line"><svg class="icon"><use href="#icon-phone"/></svg>+555 014 2276</div><br>
    <div class="contact-line"><svg class="icon"><use href="#icon-mail"/></svg>info@tandrel.com</div><br>
    <div class="contact-line"><svg class="icon"><use href="#icon-web"/></svg>www.<span class="web-strong">tandrel</span>.com</div>
  </div>
  <div class="card-address"><span class="brand">Tandrel</span> - 412 W 9th St. Ste 210 Brayford, OH 45102</div>
</section>

</body>
</html>
```